Flyer for Home Improvement Lead Generation

We need a flyer that shows people the work we do. Replacement windows doors and siding. We offer quality products and great workmanship at fair prices. The company name is Granite Ridge Remodeling. I will upload a document with some of the features we would like to show in the flyer.
Wow would like to keep a homegrown look to our marketing.
We use Georgia font in caps for our logo text.
The hex for the logo color is #F67B04
This flyer will be for lead generation so it should showcase reasons to call us.
Our web address. grr-vt.com
Our Phone number. 860-412-9368
leave a spot for a QR code.
Target Market(s)
Residential
Industry/Entity Type
Home Improvement. Replacement windows, doors and siding
Look and feel

```html
<!DOCTYPE html>
<html lang="en">
<head>
<meta charset="utf-8">
<title>Granite Ridge Remodeling – Flyer</title>
<link rel="stylesheet" href="https://fonts.googleapis.com/css2?family=Gelasio:wght@500;600;700&family=Poppins:wght@400;600;700&display=swap">
<style>
  :root {
    --stage: #8ea4a3;
    --black: #050505;
    --white: #f2f2f2;
    --orange: #e5861e;
    --brand: #f67b04;
    --ink: #111111;
    --serif: "Gelasio", Georgia, serif;
    --sans: "Poppins", Arial, sans-serif;
  }
  * { box-sizing: border-box; margin: 0; padding: 0; }
  html, body { width: 1200px; height: 1117px; overflow: hidden; }
  body { background: var(--stage); font-family: var(--sans); }

  .flyer {
    position: absolute; left: 220px; top: 21px;
    width: 760px; height: 1075px;
    background: var(--white); overflow: hidden;
  }
  .abs { position: absolute; }

  /* Header & hero */
  .top-strip { left: 0; top: 0; width: 760px; height: 17px; background: var(--black); }
  .hero {
    left: 0; top: 17px; width: 760px; height: 452px;
    background: linear-gradient(180deg, #b9cfe6 0%, #d6e2ee 22%, #7c8794 45%, #3f444b 70%, #2f3d2c 100%);
  }
  .brand-block { left: 0; top: 0; width: 342px; height: 214px; }
  .brand-mark { left: 124px; top: 40px; width: 52px; height: 52px; border-radius: 50%; background: var(--brand); }
  .brand-name {
    left: 0; top: 118px; width: 300px; text-align: center;
    font-family: var(--serif); font-weight: 500; font-size: 27px; line-height: 32px;
    color: var(--brand); text-transform: uppercase; letter-spacing: 0.5px;
  }
  .headline {
    left: 330px; top: 42px; width: 400px; text-align: center;
    font-family: var(--serif); font-weight: 700; font-size: 26px; line-height: 30px; color: var(--ink);
  }
  .headline .accent { color: var(--orange); }

  /* Intro */
  .intro {
    left: 50px; top: 487px; width: 660px; text-align: center;
    font-size: 13.3px; line-height: 16.5px; color: var(--ink);
  }
  .intro strong { color: var(--orange); font-weight: 600; }

  /* Services */
  .services-bar {
    left: 0; top: 575px; width: 760px; height: 40px; background: var(--orange);
    font-family: var(--serif); font-weight: 700; font-size: 27px; line-height: 40px;
    color: #fff; text-align: center;
  }
  .services { left: 0; top: 615px; width: 760px; height: 272px; background: var(--black); }
  .service { position: absolute; top: 15px; width: 203px; text-align: center; color: #fff; }
  .service-photo { width: 203px; height: 122px; }
  .service h3 { margin-top: 16px; font-size: 15px; line-height: 18px; font-weight: 600; }
  .service p { margin-top: 5px; font-size: 10.6px; line-height: 12.6px; padding: 0 2px; }
  .photo-windows { background: linear-gradient(180deg, #e4e6e8 0%, #a9b3a5 45%, #4a4d52 100%); }
  .photo-door { background: linear-gradient(90deg, #8a7457 0%, #4a2e1f 35%, #3a2418 65%, #8a7457 100%); }
  .photo-siding { background: linear-gradient(180deg, #9fc0e2 0%, #5e6670 50%, #3c4a37 100%); }

  /* Bottom */
  .about {
    left: 58px; top: 917px; width: 312px;
    font-size: 12px; line-height: 14px; color: var(--ink);
  }
  .contact-shape { left: 0; top: 887px; width: 760px; height: 188px; }
  .contact { left: 420px; top: 910px; width: 320px; color: #fff; }
  .contact h2 { font-family: var(--serif); font-weight: 700; font-size: 28px; line-height: 34px; }
  .contact p { margin-top: 4px; width: 252px; font-size: 9.4px; line-height: 11.6px; }
  .qr-spot {
    left: 674px; top: 914px; width: 60px; height: 60px;
    background: #fff; border: 3px solid #fff; outline: 1px dashed rgba(0,0,0,0.35); outline-offset: -7px;
  }
  .phone { margin-top: 3px; display: flex; align-items: center; gap: 6px; font-family: var(--serif); font-weight: 600; font-size: 37px; line-height: 40px; }
  .web { font-size: 14.5px; letter-spacing: 5px; line-height: 18px; }
</style>
</head>
<body>
<div class="flyer">
  <div class="abs hero" role="img" aria-label="Photo of a two-storey grey-sided home with white-trimmed windows under a blue sky"></div>
  <div class="abs top-strip"></div>

  <svg class="abs brand-block" viewBox="0 0 342 214" aria-hidden="true">
    <polygon points="0,0 342,0 273,214 0,214" fill="#050505"/>
  </svg>
  <div class="abs brand-mark"></div>
  <div class="abs brand-name">Granite Ridge<br>Remodeling</div>

  <h1 class="abs headline"><span class="accent">Quality Replacement</span><br>Windows, Doors and Siding<br>at a Fair Price!</h1>

  <p class="abs intro"><strong>Granite Ridge Remodeling</strong> is a professional home improvement contractor based in Alder Falls, VT. Our team of experts is dedicated to providing exceptional home improvement services to homeowners in Alder Falls and surrounding areas. We specialize in replacement windows, doors and siding. We take pride in our work and always strive to exceed our clients' expectations.</p>

  <h2 class="abs services-bar">Our Services</h2>
  <section class="abs services">
    <article class="service" style="left:58px">
      <div class="service-photo photo-windows" role="img" aria-label="Photo of a bright sunroom lined with replacement windows"></div>
      <h3>Replacement<br>Window Installation</h3>
      <p>Enhance energy efficiency, improve insulation, and elevate the appearance of your home with our expertly installed replacement windows.</p>
    </article>
    <article class="service" style="left:283px">
      <div class="service-photo photo-door" role="img" aria-label="Photo of a dark wooden front door set in a stone entry"></div>
      <h3>Door Replacement<br>and Installation</h3>
      <p>Our skilled team will handle every aspect of the replacement and installation process, ensuring a seamless fit and lasting performance.</p>
    </article>
    <article class="service" style="left:505px">
      <div class="service-photo photo-siding" role="img" aria-label="Photo of a house exterior with new grey siding"></div>
      <h3>Siding Replacement<br>and Upgrades</h3>
      <p>Boost curb appeal, protect your home from the elements, and increase property value with our premium siding replacement and upgrade services.</p>
    </article>
  </section>

  <svg class="abs contact-shape" viewBox="0 0 760 188" aria-hidden="true">
    <polygon points="407,16 760,16 760,170 351,170" fill="#e5861e"/>
    <rect x="0" y="170" width="760" height="18" fill="#e5861e"/>
  </svg>

  <p class="abs about">As a family-owned and -operated business based in Alder Falls, VT, we are invested in providing personalized service from Day 1. Beginning with the first conversation through project completion we'll answer your questions and resolve any concerns to ensure that you are informed and satisfied. When you reach out to our office you won't reach a large call center in a different state.</p>

  <div class="abs contact">
    <h2>Get In Touch</h2>
    <p>If you have any questions or would like to schedule an appointment for your free quote, please fill out the form below and we will get back to you as soon as possible.</p>
    <div class="phone">
      <svg width="26" height="26" viewBox="0 0 26 26" aria-hidden="true">
        <circle cx="13" cy="13" r="13" fill="#fff"/>
        <path d="M9.2 6.5c.6-.4 1.3-.2 1.6.4l1.2 2.3c.3.6.1 1.2-.4 1.6l-.9.7c.6 1.6 1.8 2.9 3.4 3.6l.7-.9c.4-.5 1.1-.6 1.6-.3l2.3 1.3c.6.3.8 1.1.4 1.6l-.8 1.1c-.6.8-1.7 1.1-2.7.7-3.8-1.4-6.6-4.3-7.9-8.1-.3-1 0-2 .8-2.6z" fill="#e5861e"/>
      </svg>
      <span>860-412-9368</span>
    </div>
    <div class="web">www.grr-vt.com</div>
  </div>
  <div class="abs qr-spot" role="img" aria-label="Space reserved for a QR code"></div>
</div>
</body>
</html>
```